Desert Basin Company Brochure

**** UPDATE 2-8-2014 ****

Size should be 11" X 17" or larger (tri or bi fold).

We're going to let the contest run it's full duration to allow for more time spent on designs.

No black backgrounds.

Consideration should be given to having the text be easy to read and in a nice, organized format.

*****************************

We're looking for an eye-catching, colorful brochure that will explain what we do, who we are... and what sets us apart from the competition.

Our company provides swimming pool service, repair, and custom renovations throughout the Phoenix, Arizona metropolitan area. These brochures will be hand-delivered to each prospective customer we visit.

The brochure will include images of our work, product logos, and a unique design that separates our company apart from the rest.

The brochure should be tri-fold. Although, if a designer wants to (or has better ideas) for a different lay-out, then we're open to seeing what can be done.

Colors we like: Blue, White, Silver, Copper, Green (accent color)

We like designs that are unique/different. Professional. Creative. Sleek. Sexy. Custom. We don't want the brochure to be "pretentious". We'd like for these brochures to leave a lasting impression with our prospective clients... and hopefully earn us more business.

We don't want the brochure to be too wordy, however if the designer feels we need to cut back (or add), let us know.

Our motto is "Every Ripple Counts Twice".

You can view some of our projects, and what we're about either at our website (brightwaveaqua.example), Chatterbook (www.chatterbook/brightwaveaqua), or Searchly+ (https://plus.google.com/+Brightwaveaqua). Thank you!

- Print-

(Front) Logo

Service - Repair - Renovation
555-731-4409
brightwaveaqua.example
service@brightwaveaqua.example
Like Us On Chatterbook! Chatterbook LOGO
Searchly Plus LOGO

(Body) Why Choose Us?

Thank you for the opportunity for our company to become your pool service provider!

We’re committed to providing the best customer service possible! At the end of the day you want your pool to be clean, clear, operational, and for your service provider to be available when you need them!

We’re licensed with the Westland Board Of Tradesmen, Bonded, and Fully Insured.
A+ reviews with the Honest Trade Council, Marla’s Picks, Wombit, Vyn, Chatterbook, and Searchly!
All technicians are employees... not sub-contractors! Our employees are hard working, dependable, professional, and expected to follow our strict protocol for servicing your pool.
Flat-fee service rates! Any additional equipment repairs, maintenance, or chemical implementations are directly authorized by you!
No contracts! Our Service Level Agreement Form allows you to select your desired level of authorization for equipment repairs, filter maintenance, and extra chemical implementation programs.
Our uniformed technicians arrive in distinctive, clean GPS-tracked company trucks.
We leave detailed service slips after each service visit. In addition, all service visit information is electronically recorded and stored.
Easy, online account management to view and pay invoices or authorize estimates.
Invoices, estimates, questions, pictures, and video are communicated via e-mail!
Free service calls to diagnose equipment issues outside of our normal service.
10% Service Client Discount for all repairs and replacement items.
Brightwave Aqua knows the importance of communication! We’re available by phone, email, or text all days of the week.

(Body) Our Methodology

We believe in 5 important factors in maintaining a clean, clear, and operational pool...

Good, Clean Water! Our local water supply contains high amounts of minerals. Pool chemicals add to this problem in a short amount of time. Our philosophy is to use the least amount of chemicals possible to achieve optimal water balance.
Efficient Water Flow! The invention of variable-speed pumps has enabled the ability to "dial in" proper water flow... while driving down energy costs.
Proper Filtration! Today’s high-capacity cartridge filters provide great filtration, save on wasted water from backwashing sand filters, and eliminate the need for water flow-restricting backwash valves.
Functioning Cleaning System! Having a working automatic cleaning system is vital in keeping the pool surface clean of debris and dirt... and free of staining.
A Dependable And Professional Pool Maintenance Technician! Our job is to not only oversee all of the items listed above... but to make sure your pool is in the best condition possible!

(Body) Equipment Repair & Installation

We’re educated on all phases of swimming pool equipment repair and installation... with a focus on energy-efficiency and optimum performance!

We’re an KTV & MWE Authorized Installer of variable-speed pool pumps. KTV & MWE trust us to properly install and calibrate all variable-speed pumps. We've been equipped to handle the new industry standards on variable-speed pumps since Arizona law went into effect January 1st, 2011.
We’re experts at acid washes and erasing the mineral build-up off of waterlines. All work is done in-house with our customized cleaning rig and trailer.
Heating systems. New efficiency standards have made installation and operation more affordable than ever.
Remote control automation systems. Technology now allows the user to easily view and control their entire pool system via a remote home computer, tablet, or phone!
Brilliant, color-changing LED lighting for pools and spas! The benefits of LED include brighter and broader displays... while lasting much longer than your typical light bulbs.
Salt systems provide a soft-water experience! In addition to the benefit of better feeling water, salt systems generate plenty of chlorine to keep your pool sanitized.

(Body) About Us

A native to Phoenix, Dorian Kessel founded Brightwave Aqua in 2000. Our company was built from the ground up by way of hard work, word of mouth, and determination. Our company will always remain firmly grounded, and continue to develop systems that put our customers first!

Our philosophy is to treat every pool as if it were our own, run an efficient and organized business, and care for our employees.

Brightwave Aqua is a yearly, proud contributor to the Saguaro Youth Medical Center Splash Smart Day. Please educate and watch all children around water... every accident can be avoided.

(Back) Contact Us
Logos To Use, Files Uploaded: Marla’s Picks, HTC, Hydrova, Searchly+, Chatterbook, KTV/MWE logo, Saguaro Youth Medical Center

Office: 555-731-4409 | Fax: 555-731-4413 | Email: service@brightwaveaqua.example
brightwaveaqua.example

Office / Warehouse Location
41276 East Cholla Street, Suite 8
Phoenix, Arizona 85999
(NW of Cholla Street & Ironwood Mesa Road)

AZ ROC: 731502, 731503, 731504, 864017

Target Market(s)

We target a market of pool owners, which typically have more disposable income.

30 - 75 years old.

Our clients range from first-time home buyers, self-employed, business professionals, doctors, landlords, thousandaires, millionaires.

Industry/Entity Type

Pool Service

Font styles to use
Serif

Colors
0355a3
cfdfed
ffffff
3176b5
eaf1f7

Requirements
Must have
• Must use provided images. We've included a few pool pictures, and will let you decide which ones to incorporate throughout the brochure.

Logos Used:
Brightwave Aqua
Hydrova
HTC
Marla's Picks
KTV
MWE
Saguaro Youth Medical Center
Searchly+
Chatterbook

Image pic of some of our trucks.

Nice to have
• Equipment images worked in.
Should not have
• Cartoonish fonts or design. No "Love" hearts!!

```html
<!DOCTYPE html>
<html lang="en">
<head>
<meta charset="utf-8">
<title>Desert Basin Company Brochure – Inside Spread</title>
<link href="https://fonts.googleapis.com/css2?family=Noto+Serif:wght@700&family=Tinos&family=Montserrat:wght@300&display=swap" rel="stylesheet">
<style>
  :root{
    --brand-blue:#0355a3;
    --text-blue:#1b5fa8;
    --sky:#cfdfed;
    --mist:#eaf1f7;
    --white:#ffffff;
    --accent-green:#9ccb3b;
    --water-deep:#5f8fb6;
    --water-mid:#8fb4d0;
    --stone:#d9cbb4;
  }
  *{margin:0;padding:0;box-sizing:border-box}
  html,body{width:1200px;height:849px;overflow:hidden;background:var(--white)}
  .spread{
    position:relative;width:1200px;height:849px;overflow:hidden;
    background:linear-gradient(to bottom,var(--sky) 0%,#d6e4f0 45%,var(--mist) 60%);
    font-family:"Tinos","Times New Roman",serif;color:var(--text-blue);
  }
  .pool-photo{
    position:absolute;left:0;top:440px;width:1200px;height:409px;
    background:
      radial-gradient(ellipse 260px 200px at 60px 330px,var(--stone) 0%,rgba(217,203,180,0) 100%),
      radial-gradient(ellipse 180px 90px at 560px 320px,#e8ddc9 0%,rgba(232,221,201,0) 100%),
      radial-gradient(ellipse 260px 120px at 1120px 230px,#eef4f8 0%,rgba(238,244,248,0) 100%),
      linear-gradient(to bottom,rgba(214,228,240,0) 0%,rgba(143,180,208,.7) 35%,var(--water-mid) 60%,var(--water-deep) 100%);
  }
  .column{position:absolute;top:62px}
  .column h2{
    font-family:"Noto Serif",Georgia,serif;font-weight:700;font-size:19px;
    line-height:20px;color:var(--brand-blue);margin-bottom:13px;
  }
  .column p{font-size:15px;line-height:14.3px}
  .column p + p{margin-top:14.3px}
  .col-methodology{left:40px;width:222px}
  .col-why{left:347px;width:510px}
  .col-equipment{left:941px;width:222px}
  .footer-band{position:absolute;top:727px;left:0;width:1200px;height:61px;display:flex}
  .social{
    width:300px;background:var(--accent-green);display:flex;align-items:center;
    padding-left:40px;gap:12px;font-size:11px;color:var(--white);
  }
  .social .mark{width:21px;height:21px;background:var(--brand-blue)}
  .motto{
    width:600px;background:var(--brand-blue);display:flex;align-items:center;justify-content:center;
    font-family:"Montserrat",Arial,sans-serif;font-weight:300;font-size:25px;
    letter-spacing:.5px;color:var(--white);
  }
</style>
</head>
<body>
<main class="spread">
  <div class="pool-photo" role="img" aria-label="Photo of a backyard pool with stone deck edge and clear blue water"></div>

  <section class="column col-methodology">
    <h2>Our Methodology</h2>
    <p>We believe in 5 important factors in maintaining a clean, clear, and operational pool...</p>
    <p>Good, Clean Water! Our local water supply contains high amounts of minerals. Pool chemicals add to this problem in a short amount of time. Our philosophy is to use the least amount of chemicals possible to achieve optimal water balance.<br>
    Efficient Water Flow! The invention of variable-speed pumps has enabled the ability to "dial in" proper water flow... while driving down energy costs.<br>
    Proper Filtration! Today’s high-capacity cartridge filters provide great filtration, save on wasted water from backwashing sand filters, and eliminate the need for water flow-restricting backwash valves.<br>
    Functioning Cleaning System! Having a working automatic cleaning system is vital in keeping the pool surface clean of debris and dirt... and free of staining.<br>
    A Dependable And Professional Pool Maintenance Technician! Our job is to not only oversee all of the items listed above... but to make sure your pool is in the best condition possible!</p>
  </section>

  <section class="column col-why">
    <h2>Why Choose Us?</h2>
    <p>Thank you for the opportunity for our company to become your pool service provider!</p>
    <p>We’re committed to providing the best customer service possible! At the end of the day you want your pool to be clean, clear, operational, and for your service provider to be available when you need them!</p>
    <p>We’re licensed with the Westland Board Of Tradesmen, Bonded, and Fully Insured.<br>
    A+ reviews with the Honest Trade Council, Marla’s Picks, Wombit, Vyn, Chatterbook, and Searchly!<br>
    All technicians are employees... not sub-contractors! Our employees are hard working, dependable, professional, and expected to follow our strict protocol for servicing your pool.<br>
    Flat-fee service rates! Any additional equipment repairs, maintenance, or chemical implementations are directly authorized by you!<br>
    No contracts! Our Service Level Agreement Form allows you to select your desired level of authorization for equipment repairs, filter maintenance, and extra chemical implementation programs.<br>
    Our uniformed technicians arrive in distinctive, clean GPS-tracked company trucks.<br>
    We leave detailed service slips after each service visit. In addition, all service visit information is electronically recorded and stored.<br>
    Easy, online account management to view and pay invoices or authorize estimates.<br>
    Invoices, estimates, questions, pictures, and video are communicated via e-mail!<br>
    Free service calls to diagnose equipment issues outside of our normal service.<br>
    10% Service Client Discount for all repairs and replacement items.<br>
    Brightwave Aqua knows the importance of communication! We’re available by phone, email, or text all days of the week.</p>
  </section>

  <section class="column col-equipment">
    <h2>Equipment Repair &amp; Installation</h2>
    <p>We’re educated on all phases of swimming pool equipment repair and installation... with a focus on energy-efficiency and optimum performance!</p>
    <p>We’re an KTV &amp; MWE Authorized Installer of variable-speed pool pumps. KTV &amp; MWE trust us to properly install and calibrate all variable-speed pumps. We've been equipped to handle the new industry standards on variable-speed pumps since Arizona law went into effect January 1st, 2011.<br>
    We’re experts at acid washes and erasing the mineral build-up off of waterlines. All work is done in-house with our customized cleaning rig and trailer.<br>
    Heating systems. New efficiency standards have made installation and operation more affordable than ever.<br>
    Remote control automation systems. Technology now allows the user to easily view and control their entire pool system via a remote home computer, tablet, or phone!<br>
    Brilliant, color-changing LED lighting for pools and spas! The benefits of LED include brighter and broader displays... while lasting much longer than your typical light bulbs.<br>
    Salt systems provide a soft-water experience! In addition to the benefit of better feeling water, salt systems generate plenty of chlorine to keep your pool sanitized.</p>
  </section>

  <footer class="footer-band">
    <div class="social"><span class="mark"></span><span>www.chatterbook/brightwaveaqua</span></div>
    <div class="motto">EVERY RIPPLE COUNTS TWICE</div>
    <div class="social"><span class="mark"></span><span>plus.searchly.example/+Brightwaveaqua</span></div>
  </footer>
</main>
</body>
</html>
```